New website for selling opensource software business to business

Website K7 Software

The open source software industry has grown enormously in recent years. More and more customers from software companies choose an open source solution. K7 Software is going to fulfill this increasing demand.

Core business

Reselling software subcriptions (business to business).

Side business

Selling consultancy and Training to customers

Goals:

- Binding of customers to K7 IT Group
- Sales of subscriptions to customer
- Enlarge network K7 IT Group
- USP: Sales of complete package, Software, consultancy and training

Products

There are a couple of products/ services that K7 will provide. Below you will find an overview of the Products:

- Bluefox subscriptions
- Crater subscriptions
- Velmor products
- Customized consultancy for the customer
- Customized training for the customer

Style

Behind the website should be a cms system like pagecraft.

Target Market(s)

Business - Business

Industry/Entity Type

Business

Coding

Coded - Design and coding required

Number of Pages Required

5+ page

Font styles to use
Other font styles liked:
• Calibri

Colors
0355a3
3176b5
85abd2

Requirements
Must have
• Home page with large photo background, About us, contact page with safe option to request more info
• Portfolio pages:
• 4 pages with a product group each:
• 1. Blue fox
• 2. Craters
• 3. Velmor
• 4. Ourtrustwall
• 1. Blue Fox
• On top space for short info/bullets about Blue fox. Further, a grid with 8 columns. In the columns 2 buttons both lead to a popup. A popup for information and a popup for requesting a quote.
• 2. Crater:
• On top space for short info/bullets about Crater. Further, a grid with 3 columns. In the columns 2 buttons both lead to a popup. A popup for information and a popup for requesting a quote.
• 1. Velmor:
• On top space for short info/bullets about Velmor. Further, a grid with 4 columns. In the columns 2 buttons both lead to a popup. A popup for information and a popup for requesting a quote.
• 2. Ourtrustwall:
• On top space for short info/bullets about Ourtrustwall. Further, a grid with 2 columns. In the columns 2 buttons both lead to a popup. A popup for information and a popup for requesting a quote.

```html
<!DOCTYPE html>
<html lang="en">
<head>
<meta charset="utf-8">
<title>K7 Software – Open source software solution</title>
<link rel="stylesheet" href="https://fonts.googleapis.com/css2?family=Open+Sans:wght@400;600&family=Source+Sans+3:wght@600;700&family=PT+Serif&display=swap">
<style>
  :root {
    --brand-blue: #0355a3;
    --mid-blue: #3176b5;
    --light-blue: #85abd2;
    --purple: #3d2a86;
    --ink: #333;
    --grey-text: #666;
    --heading-grey: #555;
    --faint-grey: #ddd;
    --footer-bg: #efefef;
    --white: #fff;
  }
  * { box-sizing: border-box; margin: 0; padding: 0; }
  html, body { width: 712px; height: 1200px; overflow: hidden; background: var(--white); }
  body { position: relative; font-family: "Open Sans", Arial, sans-serif; color: var(--ink); }
  .abs { position: absolute; }

  /* Header */
  .site-header { position: absolute; left: 0; top: 0; width: 712px; height: 90px; background: var(--white); }
  .brand { position: absolute; left: 46px; top: 9px; width: 68px; height: 68px; border-radius: 50%; background: #e6e6e6;
    display: flex; align-items: center; justify-content: center; font-family: "Source Sans 3", sans-serif; font-weight: 700;
    font-size: 26px; color: var(--brand-blue); }
  .main-nav { position: absolute; top: 37px; left: 334px; display: flex; gap: 0; font-size: 10.5px; text-transform: uppercase; }
  .main-nav a { color: #555; text-decoration: none; margin-right: 17px; }
  .main-nav a.is-active { color: var(--brand-blue); }
  .call-button { position: absolute; left: 567px; top: 32px; width: 99px; height: 27px; background: var(--brand-blue); color: var(--white);
    font-family: "Source Sans 3", sans-serif; font-weight: 700; font-size: 13px; display: flex; align-items: center; justify-content: center; }

  /* Hero */
  .hero { position: absolute; left: 0; top: 90px; width: 712px; height: 334px;
    background: linear-gradient(110deg, #3f4fa6 0%, #3a6ab8 45%, #3679c0 100%); }
  .hero-title { position: absolute; left: 45px; top: 96px; font-family: "Source Sans 3", sans-serif; font-weight: 600; font-size: 54px; color: var(--white); line-height: 1; letter-spacing: -0.5px; }
  .hero-sub { position: absolute; left: 47px; top: 155px; font-family: "Source Sans 3", sans-serif; font-weight: 600; font-size: 21px; color: var(--white); }
  .hero-button { position: absolute; left: 46px; top: 190px; width: 111px; height: 31px; background: var(--white); color: var(--brand-blue);
    font-family: "Source Sans 3", sans-serif; font-weight: 700; font-size: 13px; display: flex; align-items: center; justify-content: center; }

  /* Welcome */
  .welcome-title { position: absolute; left: 47px; top: 464px; font-family: "Source Sans 3", sans-serif; font-weight: 700; font-size: 27px; color: var(--heading-grey); }
  .welcome-title .accent { color: var(--brand-blue); }
  .welcome-title .accent-2 { color: var(--purple); }
  .welcome-text { position: absolute; left: 47px; top: 503px; width: 325px; font-size: 9.3px; line-height: 15px; color: var(--ink); }
  .goals-label { position: absolute; left: 48px; top: 550px; font-size: 12.5px; color: var(--ink); display: flex; align-items: center; }
  .goals-label::before { content: ""; width: 7px; height: 7px; border-radius: 50%; background: #999; margin-right: 5px; }
  .goals-list { position: absolute; left: 59px; top: 569px; list-style: none; font-size: 9.3px; line-height: 15.6px; color: var(--grey-text); }
  .welcome-art { position: absolute; left: 392px; top: 460px; width: 298px; height: 188px; border-radius: 6px;
    background: linear-gradient(135deg, #e9eef2 0%, #f6d8cf 55%, #d8e6ee 100%); }

  /* Business */
  .biz { position: absolute; top: 690px; width: 200px; text-align: center; font-size: 9.3px; line-height: 14.5px; color: var(--grey-text); }
  .biz-icon { width: 52px; height: 52px; margin: 0 auto 12px; }
  .biz-title { color: var(--ink); font-size: 10px; }
  .biz-divider { position: absolute; left: 356px; top: 686px; width: 1px; height: 104px; background: #ddd; }

  /* Products */
  .products-title { position: absolute; left: 0; top: 838px; width: 712px; text-align: center; font-family: "Source Sans 3", sans-serif; font-weight: 700; font-size: 40px; color: var(--faint-grey); }
  .product { position: absolute; top: 912px; width: 140px; display: flex; align-items: center; justify-content: center; gap: 7px;
    font-family: "Source Sans 3", sans-serif; font-weight: 600; font-size: 24px; color: #c8c8c8; }
  .product-dot { width: 22px; height: 22px; border-radius: 50%; background: #e2e2e2; }
  .product.is-dark { color: #111; }

  /* Footer */
  .site-footer { position: absolute; left: 0; top: 984px; width: 712px; height: 216px; background: var(--footer-bg); }
  .footer-heading { position: absolute; top: 20px; font-size: 16px; color: #555; }
  .footer-text { position: absolute; top: 51px; font-size: 9.3px; line-height: 14.6px; color: var(--grey-text); }
  .read-more { font-family: "PT Serif", serif; font-size: 9.3px; color: #444; text-decoration: underline; display: block; margin-top: 2px; }
  .contact-row { display: flex; gap: 8px; align-items: flex-start; margin-bottom: 4px; }
  .contact-row svg { flex: none; margin-top: 2px; }
  .email-field { position: absolute; left: 475px; top: 92px; width: 142px; height: 23px; border: 1px solid #777; background: var(--footer-bg);
    font-family: Arial, sans-serif; font-size: 9px; color: #333; padding: 5px 4px; }
  .subscribe-button { position: absolute; left: 476px; top: 122px; width: 86px; height: 24px; border: 1px solid #777; border-radius: 2px;
    font-family: "PT Serif", serif; font-size: 10px; color: #444; display: flex; align-items: center; justify-content: center; letter-spacing: 0.5px; }
  .footer-rule { position: absolute; left: 46px; top: 177px; width: 620px; height: 1px; background: #aaa; }
  .copyright { position: absolute; left: 0; top: 189px; width: 712px; text-align: center; font-size: 9px; color: #555; }
</style>
</head>
<body>

<header class="site-header">
  <div class="brand">K7</div>
  <nav class="main-nav">
    <a class="is-active" href="#">Home</a>
    <a href="#">About</a>
    <a href="#">Portfolio</a>
    <a href="#">Contact</a>
  </nav>
  <div class="call-button">CALL NOW</div>
</header>

<section class="hero" role="img" aria-label="Top-down view of a designer's desk with keyboard, laptop and tools, overlaid with round product icons joined by a dashed path">
  <h1 class="hero-title">K7. SOFTWARE</h1>
  <p class="hero-sub">open source software solution</p>
  <div class="hero-button">KNOW MORE</div>
</section>

<h2 class="welcome-title">Welcome to <span class="accent">K7.</span> <span class="accent-2">SOFTWARE</span></h2>
<p class="welcome-text">The open source software industry has grown enormously in recent years. More and more customers from software companies choose an open source solution. K7 Software is going to fulfill this increasing demand.</p>
<div class="goals-label">Goals</div>
<ul class="goals-list">
  <li>- Binding of customers to K7 IT Group</li>
  <li>- Sales of subscriptions to customer.</li>
  <li>- Enlarge network K7 IT Group</li>
  <li>- USP: Sales of complete package, Software, consultancy and training.</li>
</ul>
<div class="welcome-art" role="img" aria-label="Flat illustration of dashboards, charts, a speedometer, a magnifying glass and a light bulb"></div>

<div class="biz" style="left:102px">
  <svg class="biz-icon" viewBox="0 0 52 52" aria-hidden="true">
    <circle cx="26" cy="26" r="25" fill="#fff" stroke="#ddd" stroke-width="1.5"/>
    <circle cx="26" cy="26" r="12" fill="none" stroke="#0355a3" stroke-width="2"/>
    <path d="M26 19v7l5 3" fill="none" stroke="#0355a3" stroke-width="2" stroke-linecap="round"/>
  </svg>
  <div class="biz-title">Core business</div>
  Reselling software subcriptions<br>(business to business).
</div>
<div class="biz-divider"></div>
<div class="biz" style="left:434px">
  <svg class="biz-icon" viewBox="0 0 52 52" aria-hidden="true">
    <circle cx="26" cy="26" r="25" fill="#fff" stroke="#ddd" stroke-width="1.5"/>
    <rect x="15" y="16" width="22" height="13" rx="2" fill="none" stroke="#0355a3" stroke-width="2"/>
    <path d="M22 29l-3 5 7-5" fill="#0355a3"/>
    <rect x="17" y="35" width="18" height="3" rx="1.5" fill="#0355a3"/>
  </svg>
  <div class="biz-title">Side business</div>
  Selling consultancy and<br>Training to customers
</div>

<h2 class="products-title">OUR PRODUCTS</h2>
<div class="product" style="left:46px">Crater</div>
<div class="product" style="left:206px"><span class="product-dot"></span>Bluefox</div>
<div class="product is-dark" style="left:364px">Velmor</div>
<div class="product" style="left:524px">K7</div>

<footer class="site-footer">
  <h3 class="footer-heading" style="left:46px">About Us</h3>
  <div class="footer-text" style="left:47px;width:175px">
    Lorem Ipsum is simply dummy text of the printing and typesetting industry. Lorem Ipsum has been the industry's standard dummy text ever since the 1500s, when an unknown printer.
    <span class="read-more">READ MORE</span>
  </div>

  <h3 class="footer-heading" style="left:260px">Contact Info</h3>
  <div class="footer-text" style="left:261px;width:180px">
    <div class="contact-row">
      <svg width="9" height="12" viewBox="0 0 9 12" aria-hidden="true"><path d="M4.5 0A4.5 4.5 0 0 0 0 4.5C0 8 4.5 12 4.5 12S9 8 9 4.5A4.5 4.5 0 0 0 4.5 0zm0 6.3a1.8 1.8 0 1 1 0-3.6 1.8 1.8 0 0 1 0 3.6z" fill="#555"/></svg>
      <span>Lorem Ipsum is simply dummy text of the printing and typesetting.</span>
    </div>
    <div class="contact-row">
      <svg width="10" height="10" viewBox="0 0 10 10" aria-hidden="true"><path d="M2 0l2 2.5-1.2 1.3a6 6 0 0 0 3.4 3.4L7.5 6 10 8 8.5 10C4 10 0 6 0 1.5z" fill="#555"/></svg>
      <span>123 456 7890</span>
    </div>
    <div class="contact-row">
      <svg width="11" height="9" viewBox="0 0 11 9" aria-hidden="true"><rect x=".5" y=".5" width="10" height="8" fill="none" stroke="#555"/><path d="M.5.5l5 4 5-4" fill="none" stroke="#555"/></svg>
      <span>info@northridgepeak.com</span>
    </div>
  </div>

  <h3 class="footer-heading" style="left:478px">Newsletter</h3>
  <div class="footer-text" style="left:476px;width:160px">Would you like to receive exclusive access to articles, white papers and our regular?</div>
  <div class="email-field">Enter Email Id</div>
  <div class="subscribe-button">SUBSCRIBE</div>

  <div class="footer-rule"></div>
  <p class="copyright">©K7. SOFTWARE. 2017 - All Rights Reserved.</p>
</footer>

</body>
</html>
```